Design a WordPress layout for a home loans company

The home loans company in question is going through a rebrand and needs a new website layout.
Sites they like: http://www.brightkeylending.example.au/
Current logo: Attached.
Colours to be used: As per those used in logo.
Primary: #71aa3d
Secondary: #130e10
Pages to be designed:
- Homepage
- Internal services page
Menu items for display purposes:
- Home
- About Us
- Speak to a Broker
- Articles
- Contact Us
A modern design with simplicity is key.
For copy, dummy text such as Lorem ipsum will be fine.
If you would like anything elso, please ask.
Target Market(s)
25-40 year old
Mostly female
Buying their first home in most cases
Industry/Entity Type
Mortgage Brokerage
Number of Pages Required
2 page

```html
<!DOCTYPE html>
<html lang="en">
<head>
<meta charset="utf-8">
<title>Brightkey Home Loans</title>
<link rel="stylesheet" href="https://fonts.googleapis.com/css2?family=Quicksand:wght@500;700&family=Tinos:wght@700&family=Lato:wght@400;700&display=swap">
<style>
:root{
  --green:#71aa3d;
  --green-dark:#3f9a4a;
  --green-deep:#2f8a48;
  --ink:#130e10;
  --text:#555;
  --light:#f2f2f2;
  --white:#fff;
  --line:#e2e2e2;
}
*{box-sizing:border-box;margin:0;padding:0}
html,body{width:1200px;height:4401px;overflow:hidden;background:var(--white)}
body{position:relative;font-family:"Lato",sans-serif;color:var(--text)}
.abs{position:absolute}
.hero-bg{left:0;top:0;width:1200px;height:640px}
.logo{left:79px;top:28px;color:var(--white);font-family:"Quicksand",sans-serif;font-weight:700;font-size:34px;line-height:38px;display:flex;align-items:center;gap:12px}
.logo .dot{width:16px;height:16px;background:var(--white)}
.nav{top:66px;left:404px;display:flex;gap:38px;font-size:16px;color:var(--white)}
.search{left:950px;top:66px}
.enquire{left:998px;top:53px;width:120px;height:53px;background:var(--ink);color:var(--white);font-weight:700;font-size:16px;display:flex;align-items:center;justify-content:center}
.hero-title{left:79px;top:184px;font-family:"Quicksand",sans-serif;font-weight:700;font-size:44px;line-height:46px;color:var(--white)}
.hero-sub{left:79px;top:292px;width:440px;font-size:15px;line-height:25px;color:var(--white)}
.label{top:362px;font-size:14px;font-weight:700;color:var(--white)}
.input{top:400px;height:52px;background:var(--white);font-size:14px;color:#888;padding:0 14px;display:flex;align-items:center}
.find{left:79px;top:461px;width:426px;height:53px;background:var(--ink);color:var(--white);font-size:16px;font-weight:700;display:flex;align-items:center;justify-content:center}
.section-title{left:0;width:1200px;text-align:center;font-family:"Tinos",serif;font-weight:700;color:var(--ink);font-size:36px;line-height:44px}
.photo{display:block}
.feature{width:332px;text-align:center}
.feature h3{font-family:"Quicksand",sans-serif;font-size:22px;color:var(--green);font-weight:700;margin-bottom:12px}
.feature p{font-size:13px;line-height:21px;color:#666}
.diamond{width:74px;height:74px;background:var(--green);transform:rotate(45deg);border:4px solid var(--white)}
.about{left:0;top:1388px;width:1200px;height:393px;background:linear-gradient(90deg,#2c2e2d,#4a4c48 60%,#6a6c66)}
.about h2{position:absolute;left:79px;top:60px;font-family:"Tinos",serif;font-size:34px;color:var(--white)}
.about p{position:absolute;left:79px;top:122px;width:540px;font-size:13px;line-height:22px;color:#ddd}
.btn-green{background:var(--green);color:var(--white);font-weight:700;font-size:16px;display:flex;align-items:center;justify-content:center}
.tile{top:1922px;width:240px;height:243px}
.tile .img{height:166px}
.tile .cap{height:77px;background:linear-gradient(180deg,#6fb04a,#3f9a4a);color:var(--white);font-family:"Quicksand",sans-serif;font-weight:700;font-size:20px;line-height:24px;display:flex;align-items:center;justify-content:center;text-align:center}
.view-all{left:522px;top:2203px;width:156px;height:59px;background:var(--ink);color:var(--white);font-weight:700;font-size:16px;display:flex;align-items:center;justify-content:center}
.testi{left:0;top:2327px;width:1200px;height:416px;background:linear-gradient(90deg,#4f9a3c,#7cb65a 50%,#4f9a3c)}
.testi-card{left:79px;top:2470px;width:1042px;height:209px;background:var(--white)}
.avatar{left:110px;top:2509px;width:128px;height:128px;border-radius:50%;background:linear-gradient(180deg,#d9d4cc,#8c9298);border:5px solid var(--white);box-shadow:0 0 0 2px #ccc}
.testi-name{left:264px;top:2508px;font-family:"Quicksand",sans-serif;font-weight:700;font-size:24px;color:var(--green)}
.testi-role{left:264px;top:2548px;font-size:14px;color:#777}
.testi-text{left:264px;top:2580px;width:640px;font-size:14px;line-height:24px;color:#666}
.dots{left:1006px;top:2628px;display:flex;gap:6px}
.dots span{width:16px;height:16px;border-radius:50%;border:2px solid var(--green);background:var(--white)}
.dots span.on{background:var(--green)}
.article{top:2896px;width:333px;height:419px;border:1px solid var(--line);background:var(--white)}
.article .img{height:311px;position:relative}
.date{position:absolute;right:0;top:40px;width:48px;height:70px;background:var(--green);color:var(--white);text-align:center;font-size:20px;font-weight:700;line-height:26px;padding-top:8px}
.date small{display:block;font-size:12px;font-weight:400;line-height:16px}
.article h4{margin:30px 0 0 15px;font-family:"Quicksand",sans-serif;font-size:22px;color:var(--green);font-weight:700}
.article .tag{margin:8px 0 0 15px;font-size:13px;color:#777}
.contact{left:0;top:3380px;width:1200px;height:625px;background:var(--light)}
.contact-title{left:681px;top:3440px;font-family:"Tinos",serif;font-size:36px;color:var(--ink);font-weight:700}
.info{left:681px;font-size:14px;line-height:22px;color:#555;display:flex;gap:14px}
.field{background:var(--white);border:1px solid var(--line);font-size:13px;color:#999;padding:14px}
.footer{left:0;top:4005px;width:1200px;height:396px;background:linear-gradient(90deg,#71aa3d,#3c9a4c 55%,#2f8a48)}
.footer-logo{left:0;top:60px;width:1200px;justify-content:center}
.footer-nav{left:0;top:182px;width:1200px;text-align:center;font-size:15px;color:var(--white)}
.social{left:0;top:235px;width:1200px;display:flex;justify-content:center;gap:18px}
.social span{width:48px;height:48px;border-radius:50%;background:var(--white)}
.rule{left:0;top:318px;width:1200px;height:1px;background:rgba(255,255,255,.35)}
.copy{left:0;top:345px;width:1200px;text-align:center;font-size:13px;color:var(--white)}
</style>
</head>
<body>

<!-- Hero -->
<svg class="abs hero-bg" viewBox="0 0 1200 640" aria-hidden="true">
  <defs>
    <linearGradient id="heroGrad" x1="0" y1="0" x2="1" y2="0">
      <stop offset="0" stop-color="#3f9a4a"/>
      <stop offset="1" stop-color="#7db83e"/>
    </linearGradient>
  </defs>
  <path d="M0 0H1200V420C1050 560 700 640 420 610C220 590 80 560 0 520Z" fill="url(#heroGrad)"/>
</svg>

<svg class="abs" style="left:540px;top:95px" width="600" height="545" viewBox="0 0 600 545" role="img" aria-label="Photo of a smiling couple holding a small model house">
  <defs>
    <linearGradient id="coupleGrad" x1="0" y1="0" x2="1" y2="1">
      <stop offset="0" stop-color="#d8d6cf"/>
      <stop offset="0.5" stop-color="#b89b84"/>
      <stop offset="1" stop-color="#6e7a86"/>
    </linearGradient>
  </defs>
  <path d="M150 20C200 -5 330 0 420 35C520 75 590 200 580 300C565 420 440 520 320 535C220 548 110 520 60 430C10 340 20 220 70 130C95 80 120 35 150 20Z" fill="#a4cd70" opacity=".55"/>
  <path d="M165 45C215 20 330 25 410 60C500 100 555 210 548 300C538 405 430 490 322 505C230 518 130 492 90 410C48 325 58 225 100 145C120 100 140 58 165 45Z" fill="url(#coupleGrad)" stroke="#fff" stroke-width="8"/>
</svg>

<div class="abs logo"><span class="dot"></span>Brightkey Home Loans</div>
<nav class="abs nav"><span>Home</span><span>About Us</span><span>Speak to a Broker</span><span>Articles</span><span>Contact Us</span></nav>
<svg class="abs search" width="22" height="22" viewBox="0 0 22 22" aria-hidden="true"><circle cx="9" cy="9" r="7" fill="none" stroke="#fff" stroke-width="2"/><path d="M14 14L20 20" stroke="#fff" stroke-width="2"/></svg>
<div class="abs enquire">ENQUIRE</div>

<h1 class="abs hero-title">Make Your Dreams<br>Come True</h1>
<p class="abs hero-sub">Your family deserves the most comfortable house to live.We help people to start a new life in a new place!</p>
<div class="abs label" style="left:79px">Suburb/town</div>
<div class="abs label" style="left:296px">or postcode</div>
<div class="abs input" style="left:79px;width:206px">Enter a location</div>
<div class="abs input" style="left:296px;width:209px"></div>
<div class="abs find">FIND BROKER</div>

<!-- Benefits -->
<h2 class="abs section-title" style="top:735px">With a Brightkey Home Loans broker,<br>you’ll have</h2>

<div class="abs photo" style="left:79px;top:866px;width:329px;height:264px;background:linear-gradient(135deg,#e8e8e8,#9aa3ad)" role="img" aria-label="Photo of a broker meeting a couple at a desk"></div>
<div class="abs photo" style="left:434px;top:866px;width:332px;height:264px;background:linear-gradient(135deg,#f0efea,#b8b2a6)" role="img" aria-label="Photo of an adviser showing a couple through a bright home"></div>
<div class="abs photo" style="left:789px;top:866px;width:332px;height:264px;background:linear-gradient(135deg,#e4e2dc,#8f8a82)" role="img" aria-label="Photo of a couple receiving house keys from an agent"></div>
<div class="abs photo" style="left:79px;top:1120px;width:329px;height:10px;background:var(--green)"></div>
<div class="abs photo" style="left:434px;top:1120px;width:332px;height:10px;background:var(--green)"></div>
<div class="abs photo" style="left:789px;top:1120px;width:332px;height:10px;background:var(--green)"></div>

<div class="abs diamond" style="left:206px;top:1093px"></div>
<svg class="abs" style="left:224px;top:1110px" width="40" height="40" viewBox="0 0 40 40" aria-hidden="true"><circle cx="20" cy="20" r="13" fill="none" stroke="#fff" stroke-width="2.5"/><path d="M7 20H33M20 7C14 14 14 26 20 33M20 7C26 14 26 26 20 33" fill="none" stroke="#fff" stroke-width="2"/></svg>
<div class="abs diamond" style="left:563px;top:1093px"></div>
<svg class="abs" style="left:580px;top:1110px" width="40" height="40" viewBox="0 0 40 40" aria-hidden="true"><circle cx="20" cy="16" r="9" fill="none" stroke="#fff" stroke-width="2.5"/><path d="M14 24L11 35L20 31L29 35L26 24" fill="none" stroke="#fff" stroke-width="2.5"/></svg>
<div class="abs diamond" style="left:918px;top:1093px"></div>
<svg class="abs" style="left:935px;top:1110px" width="40" height="40" viewBox="0 0 40 40" aria-hidden="true"><rect x="9" y="6" width="22" height="28" fill="none" stroke="#fff" stroke-width="2.5"/><path d="M13 14L16 17L21 12M13 24L16 27L21 22M24 15H28M24 25H28" fill="none" stroke="#fff" stroke-width="2"/></svg>

<div class="abs feature" style="left:79px;top:1207px"><h3>Local experts</h3><p>With brokers all across Australia, you can be confident there is a professional near you with in-depth knowledge of your local area.</p></div>
<div class="abs feature" style="left:434px;top:1207px"><h3>Ongoing trusted advice</h3><p>We believe in the power of advice to help you both now and into the future as your circumstances and needs change.</p></div>
<div class="abs feature" style="left:789px;top:1207px"><h3>Greater choice</h3><p>Financial solutions aren’t one-size-fits all, and our extensive range of lenders and products ensures we have the right solution for each individual.</p></div>

<!-- About -->
<section class="abs about">
  <h2>About Brightkey Home Loan</h2>
  <p>Lorem Ipsum is simply dummy text of the printing and typesetting industry. Lorem Ipsum has been the industry’s standard dummy text ever since the 1500s, when an unknown printer took a galley of type and scrambled it to make a type specimen book. It has survived not only five centuries, but also the leap into electronic typesetting, remaining essentially unchanged.</p>
  <div class="abs btn-green" style="left:79px;top:273px;width:153px;height:56px">READ MORE</div>
  <div class="abs" style="left:690px;top:30px;width:440px;height:310px;background:radial-gradient(ellipse at 60% 45%,#d26a3a 0,#b5b0a6 45%,rgba(74,76,72,0) 72%)" role="img" aria-label="Illustration of a house with a set of keys"></div>
</section>

<!-- Loan options -->
<h2 class="abs section-title" style="top:1830px">Compare hundreds of home loan options</h2>
<div class="abs tile" style="left:79px"><div class="img" style="background:linear-gradient(135deg,#c8a67e,#7b6a58)" role="img" aria-label="Photo of a couple unpacking boxes in a new home"></div><div class="cap">Buying your first<br>home</div></div>
<div class="abs tile" style="left:346px"><div class="img" style="background:linear-gradient(135deg,#e2c15a,#8a6a4a)" role="img" aria-label="Photo of a family reviewing finances together"></div><div class="cap">Refinancing &amp;<br>releasing equity</div></div>
<div class="abs tile" style="left:613px"><div class="img" style="background:linear-gradient(135deg,#d8d4cc,#6f6a62)" role="img" aria-label="Photo of a couple meeting an agent at a front door"></div><div class="cap">Buying your next<br>home</div></div>
<div class="abs tile" style="left:881px"><div class="img" style="background:linear-gradient(180deg,#b9d6ee,#7ea95a)" role="img" aria-label="Photo of a white house with a green lawn"></div><div class="cap">Buying an<br>investment property</div></div>
<div class="abs view-all">VIEW ALL</div>

<!-- Testimonials -->
<section class="abs testi" role="img" aria-label="Green tinted photo of a house porch with columns"></section>
<h2 class="abs section-title" style="top:2384px;color:var(--white)">Happy Customers Say</h2>
<div class="abs testi-card"></div>
<div class="abs avatar" role="img" aria-label="Portrait photo of the client"></div>
<div class="abs testi-name">Daniel Merritt</div>
<div class="abs testi-role">Client</div>
<p class="abs testi-text">Finding a way to pay for my expensive home purchase was made possible only thanks to this institution! They were the only place to accept my request!</p>
<div class="abs dots"><span></span><span class="on"></span><span></span></div>

<!-- Articles -->
<h2 class="abs section-title" style="top:2805px">Recent Articles</h2>
<article class="abs article" style="left:79px"><div class="img" style="background:linear-gradient(135deg,#eee9e0,#a7998a)" role="img" aria-label="Photo of a family saving coins in a piggy bank"><div class="date">20<small>July</small></div></div><h4>Secure Your Future</h4><p class="tag">Budgeting</p></article>
<article class="abs article" style="left:434px"><div class="img" style="background:linear-gradient(180deg,#c9d6de,#b7ae9c)" role="img" aria-label="Photo of a senior couple walking on a beach"><div class="date">20<small>July</small></div></div><h4>5 Tips For Saving Money</h4><p class="tag">Advices, Money hacks</p></article>
<article class="abs article" style="left:789px"><div class="img" style="background:linear-gradient(135deg,#5c6a86,#d9c7b2)" role="img" aria-label="Photo of a couple with a laptop in bed"><div class="date">20<small>July</small></div></div><h4>Family Budget Solutions</h4><p class="tag">Money hacks</p></article>

<!-- Contact -->
<section class="abs contact"></section>
<div class="abs" style="left:0;top:3380px;width:660px;height:625px;background:linear-gradient(90deg,#cfd3d8,#b4a79a 55%,rgba(242,242,242,0))" role="img" aria-label="Photo of a team of smiling business people"></div>
<h2 class="abs contact-title">Contact Us Now</h2>
<div class="abs info" style="top:3500px"><svg width="16" height="22" viewBox="0 0 16 22" aria-hidden="true"><path d="M8 0C3.6 0 0 3.4 0 7.8C0 13 8 22 8 22S16 13 16 7.8C16 3.4 12.4 0 8 0Z" fill="#71aa3d"/><circle cx="8" cy="8" r="3" fill="#fff"/></svg><span>Level 3, 17 Harbour Lane,<br>Northcote, Auckland 0627</span></div>
<div class="abs info" style="top:3574px"><svg width="16" height="16" viewBox="0 0 16 16" aria-hidden="true"><path d="M3 1L6 4L4.5 6.5C5.5 8.5 7.5 10.5 9.5 11.5L12 10L15 13L13 15C7 15 1 9 1 3Z" fill="#71aa3d"/></svg><span>555-201-7788</span></div>
<div class="abs info" style="top:3606px"><svg width="16" height="14" viewBox="0 0 16 14" aria-hidden="true"><rect x="0" y="1" width="16" height="12" fill="#71aa3d"/><path d="M0 2L8 8L16 2" fill="none" stroke="#fff" stroke-width="1.5"/></svg><span>contact@brightkeyhome.example</span></div>
<div class="abs field" style="left:675px;top:3662px;width:446px;height:53px">Name :</div>
<div class="abs field" style="left:675px;top:3724px;width:220px;height:53px">Name :</div>
<div class="abs field" style="left:901px;top:3724px;width:220px;height:53px">Name :</div>
<div class="abs field" style="left:675px;top:3786px;width:446px;height:78px">Name :</div>
<div class="abs btn-green" style="left:675px;top:3885px;width:176px;height:50px">SUBMIT NOW</div>

<!-- Footer -->
<footer class="abs footer">
  <div class="abs logo footer-logo"><span class="dot"></span>Brightkey Home Loans</div>
  <div class="abs footer-nav">Home &nbsp;&nbsp;|&nbsp;&nbsp; About Us &nbsp;&nbsp;|&nbsp;&nbsp; Speak to a Broker &nbsp;&nbsp;|&nbsp;&nbsp; Articles &nbsp;&nbsp;|&nbsp;&nbsp; Contact Us</div>
  <div class="abs social"><span></span><span></span><span></span><span></span></div>
  <div class="abs rule"></div>
  <div class="abs copy">Copyright © Brightkey Home Loans · 2018 . All Right reserved</div>
</footer>

</body>
</html>
```